Design an artistic, fresh and fun image/logo for an Art Box and make a little child smile

We need a logo and whole box design for a new company based in Australia named Pommelin Box. We will deliver this box to children aged 5-9 and it will contain high quality art materials. There are 3 projects in the box plus a starter kit and a bonus lesson. Once the children receive their box they are provided with detailed instruction about about the project including how to use the materials and tools and learn about famous artists and artistic styles. The art projects are educational yet fun and designed to meet the requirements of the Wendrel Learning Framework.

Target Market(s)

Parents and Grandparents of children aged 5-9.

Colors

Designer to choose colors to be used in the design.

Requirements
Must have
• A logo/font that appeals to children yet still matches with the artistic box design.
• Designer please note: starter kit, 3 projects and a bonus project must be listed on the side of the one box at the front.
• A landscape design that faces the opening of the box.
• The box should be very artistic and inspire creativity.
• happiness and fun
• colourful and eye catching
Nice to have
• use of an art style for example printmaking or collage (see images attached)
Should not have
• hand prints with paint
• Should not have an exclusive focus on general items children are familiar with including images of animals. The focus should at all times be directed towards art.
• This product is for children aged 5-9 years who want to have fun but also feel grown up and in charge of their learning. A look revolving around animals and play toys for babies and toddlers under 5 years is not appropriate.
• The box will be used every quarter with different materials and lessons so needs to relate to the Arts generally rather than focussing on one lesson.

```html
<!DOCTYPE html>
<html lang="en">
<head>
<meta charset="utf-8">
<title>Pommelin Box – Lid</title>
<link rel="stylesheet" href="https://fonts.googleapis.com/css2?family=Lilita+One&family=Patrick+Hand&display=swap">
<style>
  :root {
    --page: #ffffff;
    --lime: #9ee21f;
    --lime-light: #b8ec52;
    --lime-dark: #7cc414;
    --cream: #f8f2cf;
    --cream-edge: #e6dca6;
    --ink: #3a2a1a;
    --red: #e2343a;
    --green-text: #3fa83c;
    --badge: #6b3a1e;
    --logo: #d92a7a;
    --white: #ffffff;
    --ornament-a: #c6ee7a;
    --ornament-b: #f3c3d2;
  }
  * { box-sizing: border-box; margin: 0; padding: 0; }
  html, body { width: 1200px; height: 1200px; overflow: hidden; background: var(--page); }
  .canvas { position: relative; width: 1200px; height: 1200px; }

  .lid {
    position: absolute; left: 50px; top: 230px; width: 1100px; height: 740px;
    background: var(--lime); overflow: hidden; border-radius: 6px;
  }
  .lid__stripes {
    position: absolute; right: 120px; top: 0; width: 420px; height: 300px;
    background: repeating-linear-gradient(90deg, var(--lime-light) 0 38px, transparent 38px 76px);
    opacity: .7;
    -webkit-mask-image: linear-gradient(180deg, #000 40%, transparent);
            mask-image: linear-gradient(180deg, #000 40%, transparent);
  }
  .lid__trail { position: absolute; inset: 0; }

  .owner-tag {
    position: absolute; left: 40px; top: 90px; width: 300px; height: 118px;
    background: var(--white); border-radius: 18px;
    box-shadow: 0 0 0 6px var(--lime-light);
    padding: 18px 24px; font-family: "Patrick Hand", cursive;
  }
  .owner-tag__title { color: var(--red); font-size: 30px; line-height: 1; }
  .owner-tag__label { color: var(--green-text); font-size: 22px; }
  .owner-tag__line { margin-top: 20px; border-bottom: 2px dashed var(--lime-dark); }
  .age-badge {
    position: absolute; left: 310px; top: 62px; width: 58px; height: 58px;
    border-radius: 50%; background: var(--badge); color: var(--white);
    font: 26px/58px "Lilita One", sans-serif; text-align: center;
  }

  .brand {
    position: absolute; left: 600px; top: 50px; width: 440px; text-align: center;
    font-family: "Lilita One", sans-serif;
  }
  .brand__name { color: var(--logo); font-size: 76px; line-height: 1; letter-spacing: 2px; }
  .brand__tagline {
    margin-top: 18px; color: var(--green-text); font-size: 31px; letter-spacing: 1px;
    text-transform: uppercase; -webkit-text-stroke: 1px var(--white);
  }

  .ornament-art {
    position: absolute; left: 900px; top: 195px; width: 120px; height: 120px;
    border-radius: 14px;
    background: linear-gradient(160deg, var(--ornament-a) 0%, var(--ornament-b) 100%);
  }
  .craft-art {
    position: absolute; left: 40px; top: 300px; width: 460px; height: 350px; border-radius: 20px;
    background: linear-gradient(135deg, #aee6f2 0%, #c9d98a 50%, #b98ad8 100%); opacity: .85;
  }

  .contents {
    position: absolute; left: 760px; top: 330px; width: 320px; height: 230px;
    background: var(--cream); border: 3px solid var(--cream-edge); border-radius: 14px;
    padding: 16px 18px; transform: rotate(-2deg);
    font-family: "Patrick Hand", cursive; color: var(--ink);
  }
  .contents__list { list-style: none; }
  .contents__item { display: flex; gap: 8px; align-items: flex-start; font-size: 22px; line-height: 1.05; margin-bottom: 8px; }
  .contents__item small { display: block; font-size: 15px; }
  .tick { flex: none; width: 18px; height: 18px; margin-top: 2px; }

  .warning {
    position: absolute; left: 40px; top: 672px; display: flex; align-items: center; gap: 8px;
    background: var(--white); border-radius: 4px; padding: 3px 12px;
    font: 14px "Patrick Hand", cursive; color: var(--ink);
  }
  .warning__icon { width: 16px; height: 16px; border-radius: 50%; background: var(--ink); }
</style>
</head>
<body>
<main class="canvas">
  <section class="lid">
    <div class="lid__stripes"></div>

    <svg class="lid__trail" width="1100" height="740" viewBox="0 0 1100 740" aria-hidden="true">
      <path d="M40 290 C 220 250, 380 300, 560 280 S 820 240, 900 236" fill="none" stroke="#ffffff" stroke-width="3" stroke-dasharray="12 9"/>
      <path d="M520 740 a 40 40 0 0 1 80 0" fill="none" stroke="#6aae10" stroke-width="2"/>
    </svg>

    <div class="owner-tag">
      <p class="owner-tag__title">Beware!</p>
      <p class="owner-tag__label">This box belong to:</p>
      <div class="owner-tag__line"></div>
    </div>
    <div class="age-badge">5+</div>

    <header class="brand">
      <h1 class="brand__name">Pommelin</h1>
      <p class="brand__tagline">Home is where the art is.</p>
    </header>

    <div class="ornament-art" role="img" aria-label="Decorative paper flower ornaments and a blue paper triangle"></div>
    <div class="craft-art" role="img" aria-label="Collage illustration of paper triangles, paintbrushes, buttons and confetti dots"></div>

    <aside class="contents">
      <ul class="contents__list">
        <li class="contents__item"><svg class="tick" viewBox="0 0 18 18"><path d="M2 9 l5 5 L16 3" fill="none" stroke="#47a52b" stroke-width="3"/></svg><span>Starter kit.</span></li>
        <li class="contents__item"><svg class="tick" viewBox="0 0 18 18"><path d="M2 9 l5 5 L16 3" fill="none" stroke="#47a52b" stroke-width="3"/></svg><span>Lesson 1<small>Mixed Media: Castellane Cathedral</small></span></li>
        <li class="contents__item"><svg class="tick" viewBox="0 0 18 18"><path d="M2 9 l5 5 L16 3" fill="none" stroke="#47a52b" stroke-width="3"/></svg><span>Lesson 2<small>Art History: Verhoef</small></span></li>
        <li class="contents__item"><svg class="tick" viewBox="0 0 18 18"><path d="M2 9 l5 5 L16 3" fill="none" stroke="#47a52b" stroke-width="3"/></svg><span>Lesson 3<small>Collage: Dragonflies and Bulrushes</small></span></li>
        <li class="contents__item"><svg class="tick" viewBox="0 0 18 18"><path d="M2 9 l5 5 L16 3" fill="none" stroke="#47a52b" stroke-width="3"/></svg><span>Bonus lesson</span></li>
      </ul>
    </aside>

    <p class="warning"><span class="warning__icon"></span>Warning: Choking hazard – small parts. Not suitable for children under 3 years.</p>
  </section>
</main>
</body>
</html>
```